A picture window of stained glass as seen in older churches,
Etched in it is the tree of life.
God lead ministry

Industry/Entity Type

Ministry

Contact Information for Business Card

Morning Lantern/Quiet Harbor. Ministries
Meryl Ashdown, Founder
P.O. Box 47208 Colorado Springs, CO 80917-5520
719-555-0184

Font styles to use
Sans Serif

```html
<!DOCTYPE html>
<html lang="en">
<head>
<meta charset="utf-8">
<title>Morning Lantern – Business Card</title>
<link rel="stylesheet" href="https://fonts.googleapis.com/css2?family=Lato:wght@300;400;700;900&display=swap">
<style>
  :root {
    --backdrop: #6f6f6f;
    --card-black: #121212;
    --title-green: #63a35c;
    --band-green: #3f7e38;
    --band-edge: #24501f;
    --text-white: #f2f2f2;
    --text-soft: #d8d8d8;
    --text-muted: #a9a9a9;
    --glass-dark: #1d2a1c;
    --glass-leaf: #4f7f45;
    --glass-pale: #d9dddb;
    --glass-mist: #c3cec0;
  }
  html, body {
    margin: 0;
    padding: 0;
    width: 1200px;
    height: 900px;
    overflow: hidden;
    background: var(--backdrop);
  }
  .canvas {
    position: relative;
    width: 1200px;
    height: 900px;
  }
  .business-card {
    position: absolute;
    left: 100px;
    top: 164px;
    width: 1000px;
    height: 572px;
    background: var(--card-black);
    overflow: hidden;
    font-family: "Lato", sans-serif;
    box-shadow: 0 18px 40px rgba(0,0,0,0.35);
  }
  .window-artwork {
    position: absolute;
    left: 0;
    top: 0;
    width: 470px;
    height: 488px;
    background: linear-gradient(180deg,
      var(--glass-dark) 0%,
      var(--glass-leaf) 22%,
      var(--glass-pale) 48%,
      var(--glass-pale) 70%,
      var(--glass-mist) 88%,
      var(--glass-dark) 100%);
  }
  .ministry-title {
    position: absolute;
    left: 545px;
    top: 112px;
    margin: 0;
    color: var(--title-green);
    font-weight: 700;
    font-size: 38px;
    letter-spacing: 0.5px;
    text-transform: uppercase;
    line-height: 1;
  }
  .ministry-subtitle {
    position: absolute;
    left: 547px;
    top: 158px;
    margin: 0;
    color: var(--text-soft);
    font-weight: 400;
    font-size: 21px;
    letter-spacing: 0.8px;
    line-height: 1.2;
  }
  .contact-name {
    position: absolute;
    left: 545px;
    top: 262px;
    margin: 0;
    color: var(--text-white);
    font-weight: 300;
    font-size: 38px;
    line-height: 1.1;
  }
  .contact-name .surname { font-weight: 700; }
  .contact-role {
    position: absolute;
    left: 547px;
    top: 310px;
    margin: 0;
    color: var(--text-muted);
    font-weight: 400;
    font-size: 19px;
    letter-spacing: 1px;
    line-height: 1.2;
  }
  .contact-phone {
    position: absolute;
    left: 545px;
    top: 372px;
    display: flex;
    align-items: center;
    gap: 12px;
    color: var(--text-white);
    font-size: 24px;
    font-weight: 400;
    line-height: 1.2;
  }
  .contact-phone svg { width: 22px; height: 22px; }
  .address-band {
    position: absolute;
    left: 0;
    bottom: 0;
    width: 100%;
    height: 84px;
    background: var(--band-green);
    border-top: 8px solid var(--band-edge);
    display: flex;
    align-items: center;
    box-sizing: border-box;
    padding-left: 48px;
    gap: 22px;
  }
  .address-band svg { width: 24px; height: 32px; flex: none; }
  .postal-address {
    color: var(--text-white);
    font-weight: 700;
    font-size: 27px;
    letter-spacing: 2px;
    text-transform: uppercase;
    white-space: nowrap;
  }
</style>
</head>
<body>
  <div class="canvas">
    <div class="business-card">
      <div class="window-artwork" role="img" aria-label="Stained glass church window showing the tree of life"></div>

      <h1 class="ministry-title">Morning Lantern</h1>
      <p class="ministry-subtitle">Quiet Harbor. Ministries</p>

      <p class="contact-name">Meryl <span class="surname">Ashdown</span></p>
      <p class="contact-role">Founder</p>

      <div class="contact-phone">
        <svg viewBox="0 0 24 24" aria-hidden="true">
          <path fill="#63a35c" d="M3 8c0-2 3-4 9-4s9 2 9 4v2h-4V8.5c-1.5-.6-3-.9-5-.9s-3.5.3-5 .9V10H3zM7 11h10l3 8H4z"/>
          <circle cx="12" cy="15" r="2" fill="#121212"/>
        </svg>
        <span>719-555-0184</span>
      </div>

      <div class="address-band">
        <svg viewBox="0 0 24 32" aria-hidden="true">
          <path fill="#ffffff" d="M12 0C5.4 0 0 5.2 0 11.7 0 20 12 32 12 32s12-12 12-20.3C24 5.2 18.6 0 12 0z"/>
          <circle cx="12" cy="11.5" r="4.5" fill="#3f7e38"/>
        </svg>
        <span class="postal-address">P.O. Box 47208 Colorado Springs, CO 80917-5520</span>
      </div>
    </div>
  </div>
</body>
</html>
```